Marbury 720 - Strategic Planning Consulting - Business Card Design

We need a business card design for a national public affairs consulting firm. We specialize in strategic planning for non-profit organizations including designing winning advocacy and communications campaigns. I'd like the design to be fresh and use the logo colors and the card should have rounded edges. On the back of the card I'd like a few words that help folks understand our services:

Strategic Planning
Advocacy Campaigns
Communications
Updates

Thank you to all the designers for your amazing work.  I wish I could select all of your talented designs.

Target Market(s)

The target customer is a CEO or VP of Public Policy or Communications.

Industry/Entity Type

Communications

Requirements
Must have
• Include:

LOGO

Loretta K. Vanhorn
President/CEO

4853 SE 17th Lane
Boca Raton, FL 33428

561.374.2096

Loretta@Marbury720.com
www.Marbury720.com

On back of card:
Strategic Planning
Advocacy Campaigns
Communications

```html
<!DOCTYPE html>
<html lang="en">
<head>
<meta charset="utf-8">
<title>Marbury 720 – Business Card</title>
<link rel="stylesheet" href="https://fonts.googleapis.com/css2?family=Questrial&display=swap">
<style>
  :root {
    --page: #f2f2f3;
    --card-front: #ffffff;
    --card-front-shade: #ececee;
    --purple: #8a5ca6;
    --charcoal: #58585a;
    --band: #6b6b6d;
    --back-dark: #3a3a3c;
    --back-mid: #555557;
    --back-text: #f4f4f4;
    --back-mark: rgba(255, 255, 255, 0.06);
  }
  * { box-sizing: border-box; margin: 0; padding: 0; }
  html, body {
    width: 1200px; height: 900px; overflow: hidden;
    background: var(--page);
    font-family: "Questrial", "Century Gothic", sans-serif;
  }
  .canvas {
    position: relative; width: 1200px; height: 900px;
    display: flex; align-items: center; justify-content: center; gap: 44px;
  }
  .card {
    position: relative; width: 525px; height: 300px;
    border-radius: 22px; overflow: hidden;
    box-shadow: 0 10px 28px rgba(0,0,0,0.14);
  }
  /* Front */
  .card-front {
    background: linear-gradient(180deg, var(--card-front) 0%, var(--card-front) 60%, var(--card-front-shade) 100%);
  }
  .brand {
    position: absolute; left: 26px; top: 66px;
  }
  .brand-name {
    font-size: 44px; color: var(--purple); line-height: 1; white-space: nowrap;
  }
  .person {
    position: absolute; right: 26px; top: 24px; text-align: right;
  }
  .person-name { font-size: 19px; color: var(--charcoal); }
  .person-title { font-size: 15px; color: var(--purple); margin-top: 4px; }
  .band {
    position: absolute; left: 0; right: 0; top: 146px; height: 10px;
    background: var(--band);
  }
  .contact {
    position: absolute; left: 22px; top: 168px; list-style: none;
    font-size: 13.5px; color: var(--charcoal); line-height: 1.35;
  }
  .contact li { display: flex; align-items: flex-start; gap: 6px; }
  .contact li + li { margin-top: 8px; }
  .contact li.tight { margin-top: 2px; }
  .contact svg { width: 14px; height: 14px; flex: none; margin-top: 2px; fill: var(--purple); }
  /* Back */
  .card-back {
    background: radial-gradient(ellipse at 55% 45%, var(--back-mid) 0%, var(--back-dark) 100%);
  }
  .back-texture { position: absolute; inset: 0; }
  .back-mark {
    position: absolute; left: 0; right: 0; bottom: 26px; text-align: center;
    font-size: 68px; color: var(--back-mark); line-height: 1; white-space: nowrap;
  }
  .services {
    position: absolute; left: 0; right: 0; top: 82px; text-align: center;
    list-style: none; color: var(--back-text); font-size: 19px; letter-spacing: 2px;
  }
  .services li + li { margin-top: 10px; }
</style>
</head>
<body>
<main class="canvas">
  <section class="card card-front" aria-label="Card front">
    <div class="person">
      <div class="person-name">Loretta K. Vanhorn</div>
      <div class="person-title">President/CEO</div>
    </div>
    <div class="brand">
      <span class="brand-name">Marbury 720</span>
    </div>
    <div class="band"></div>
    <ul class="contact">
      <li>
        <svg viewBox="0 0 16 16" aria-hidden="true"><path d="M8 1 0 8h2v7h4v-4h4v4h4V8h2z"/></svg>
        <span>4853 SE 17th Lane<br>Boca Raton, FL 33428</span>
      </li>
      <li>
        <svg viewBox="0 0 16 16" aria-hidden="true"><path d="M3.5 1 6 3.5 4.5 6c1 2 3.5 4.5 5.5 5.5L12.5 10 15 12.5 13 15C7 15 1 9 1 3z"/></svg>
        <span>561.374.2096</span>
      </li>
      <li>
        <svg viewBox="0 0 16 16" aria-hidden="true"><path d="M1 3h14v10H1zM2 4.2V5l6 4 6-4v-.8L8 8z" fill-rule="evenodd"/></svg>
        <span>Loretta@Marbury720.com</span>
      </li>
      <li class="tight">
        <svg viewBox="0 0 16 16" aria-hidden="true"><path d="M8 1a7 7 0 1 0 0 14A7 7 0 0 0 8 1zm0 1.3c.8 0 1.7 1.6 2 3.7H6c.3-2.1 1.2-3.7 2-3.7zM2.4 7h3.5v2H2.4a5.7 5.7 0 0 1 0-2zm4.6 0h2v2H7zm3.1 0h3.5a5.7 5.7 0 0 1 0 2h-3.5zM6 10h4c-.3 2.1-1.2 3.7-2 3.7S6.3 12.1 6 10z"/></svg>
        <span>www.Marbury720.com</span>
      </li>
    </ul>
  </section>

  <section class="card card-back" aria-label="Card back">
    <div class="back-texture" role="img" aria-label="Fine dotted texture over charcoal gray"></div>
    <div class="back-mark" aria-hidden="true">Marbury 720</div>
    <ul class="services">
      <li>Strategic Planning</li>
      <li>Advocacy Campaigns</li>
      <li>Communications</li>
    </ul>
  </section>
</main>
</body>
</html>
```